Talvero

I'd like new business card design options. I'll need to provide updated contact info although after the deign is complete. We are in IT, specifically in the data backup, archiving and disaster recovery verticals.

Business

```html
<!DOCTYPE html>
<html lang="en">
<head>
<meta charset="utf-8">
<title>Talvero Business Cards</title>
<link rel="stylesheet" href="https://fonts.googleapis.com/css2?family=Open+Sans:wght@400;600&display=swap">
<style>
  :root {
    --backdrop: #3a3431;
    --card-dark: #111213;
    --card-light: #f1f1f1;
    --accent-blue: #2f8ee0;
    --text-light: #e8e8e8;
    --text-dark: #2b2b2b;
  }
  * { margin: 0; padding: 0; box-sizing: border-box; }
  html, body { width: 1200px; height: 900px; overflow: hidden; }
  body {
    background: var(--backdrop);
    font-family: "Open Sans", sans-serif;
    position: relative;
  }
  .card {
    position: absolute;
    width: 520px;
    height: 300px;
    top: 300px;
    border-radius: 4px;
  }
  .card--back { left: 50px; background: var(--card-dark); }
  .card--front { left: 630px; background: var(--card-light); }

  .company-name {
    font-family: "Open Sans", sans-serif;
    font-weight: 600;
    color: var(--accent-blue);
    font-size: 30px;
    line-height: 1;
  }
  .card--back .company-name { position: absolute; left: 40px; top: 176px; }
  .card--front .company-name {
    position: absolute; left: 0; right: 0; top: 110px; text-align: center; font-size: 34px;
  }

  .divider {
    position: absolute; left: 290px; top: 60px;
    width: 1px; height: 180px; background: var(--accent-blue);
  }
  .contact { position: absolute; left: 310px; top: 62px; color: var(--text-light); }
  .contact__name {
    color: var(--accent-blue); font-size: 19px; letter-spacing: 0.5px; line-height: 1.1;
  }
  .contact__role { font-size: 14px; margin-bottom: 8px; }
  .contact__list { list-style: none; font-size: 15px; line-height: 1.35; }
  .contact__list li { display: flex; align-items: center; gap: 8px; }
  .contact__list svg { width: 12px; height: 12px; fill: var(--accent-blue); flex: none; }
  .contact__address { font-size: 15px; line-height: 1.35; margin-top: 10px; }

  .services {
    position: absolute; left: 0; right: 0; top: 220px;
    text-align: center; color: var(--text-dark); font-size: 13px;
  }
</style>
</head>
<body>
  <section class="card card--back">
    <p class="company-name">Talvero</p>
    <span class="divider"></span>
    <div class="contact">
      <p class="contact__name">MARCUS ELLORY</p>
      <p class="contact__role">Managing Director</p>
      <ul class="contact__list">
        <li><svg viewBox="0 0 12 12"><path d="M1 4c0-2 2-3 5-3s5 1 5 3l-2 1-1-2H4L3 5zM3 6h6l1 5H2z"/></svg>(044)123456789</li>
        <li><svg viewBox="0 0 12 12"><rect x="3" y="0" width="6" height="12" rx="1"/></svg>(044)123456789</li>
        <li><svg viewBox="0 0 12 12"><path d="M0 2h12v8H0z M0 2l6 5 6-5" stroke="#111213" stroke-width="1"/></svg>hello@talvero-mail.com</li>
        <li><svg viewBox="0 0 12 12"><circle cx="6" cy="6" r="6"/></svg>www.talvero-data.com</li>
      </ul>
      <p class="contact__address">1234, Address GoesHere,<br>Country name, 12345</p>
    </div>
  </section>

  <section class="card card--front">
    <p class="company-name">Talvero</p>
    <p class="services">Disaster Recovery Server Backup and Archiving Solutions</p>
  </section>
</body>
</html>
```